Bahamas Pharmacy needs Flyer to Promote "Blood Pressure Tracking Service"

We need a double sided flyer design 5.5" x 8.5" (redesign) to promote a "Blood Pressure Tracking Service". Persons that have a card will be able to track their blood pressure online through a secure online blood pressure tracker. Clients of Brightwell Care Pharmacy will be to test themselves--so information is confidential. Test Regularly - their information is stored up to 30 readings. Share the printed results. Flyer must contain endorsement logos of Coral Reach Cardiac Association Flyer and Coral Reach Sugar Care Association. The final design should communicate responsible tracking of health of elders and parents look clean, crisp, elegant modern yet simplistic. Any imagery should be friendly to the mixed-race demographic of the Bahamas. Contain imagery on either side of "Chatterloop and Pipsqueal"

Target Market(s)

Families

Industry/Entity Type

Health

Font styles to use
Sans Serif

Colors
0255a3
9ccb3b
ffffff
ec2027

Requirements
Must have
• Images of Happy African-American or Mixed-Race Family, Similar Aesthetic to "Perks Circle" flyer
Nice to have
• Imagery of Nurse taking blood pressure monitor, please see example of imagery type to be used.
Should not have
• Too much text, Small Imagery,

```html
<!DOCTYPE html>
<html lang="en">
<head>
<meta charset="utf-8">
<title>Brightwell Care Pharmacy – Blood Pressure Tracking Service</title>
<link rel="stylesheet" href="https://fonts.googleapis.com/css2?family=Lato:wght@400;700;900&display=swap">
<style>
  :root{
    --red:#e2232a;
    --green:#6fb22c;
    --lime-text:#d8ee5a;
    --white:#ffffff;
    --page:#ffffff;
  }
  *{margin:0;padding:0;box-sizing:border-box}
  html,body{width:851px;height:1200px;overflow:hidden;background:var(--page)}
  body{font-family:"Lato",sans-serif;color:var(--white)}
  .flyer{position:relative;width:851px;height:1200px;overflow:hidden;background:var(--red)}
  .header{position:absolute;left:0;top:0;width:100%;height:160px;background:var(--white)}
  .brand-title{position:absolute;left:48px;top:26px;color:var(--red);font-weight:900;font-size:52px;line-height:1.05;letter-spacing:-.5px}
  .logo-tab{position:absolute;left:640px;top:22px;width:185px;height:175px;background:var(--white);border:5px solid var(--red);border-radius:0 0 0 60px;display:flex;flex-direction:column;align-items:center;justify-content:center;gap:10px;z-index:3}
  .logo-mark{width:56px;height:56px;border-radius:50%;background:var(--red)}
  .logo-name{color:var(--red);font-weight:700;font-size:22px}
  .shapes{position:absolute;left:0;top:0;width:851px;height:1200px}
  .side-note{position:absolute;left:664px;top:215px;width:600px;height:150px;transform-origin:0 0;transform:translate(150px,0) rotate(90deg);font-size:19px;line-height:1.3;font-weight:700;text-transform:uppercase;color:var(--white);z-index:2}
  .service{position:absolute;left:40px;top:582px;width:600px}
  .service-title{font-weight:900;font-size:40px;line-height:1.1;white-space:nowrap}
  .service-lead{margin-top:6px;color:var(--lime-text);font-weight:700;font-size:20px;line-height:1.2}
  .service-body{position:absolute;left:40px;top:716px;width:600px;font-size:19px;line-height:1.3;text-align:center}
  .footer-text{position:absolute;left:40px;top:1010px;width:520px;font-size:21px;line-height:1.3}
  .contact{position:absolute;left:40px;top:1126px;display:flex;align-items:center;gap:14px;font-weight:700;font-size:30px}
  .contact svg{width:34px;height:34px}
  .contact .gap{width:30px}
</style>
</head>
<body>
<main class="flyer">
  <div class="header">
    <h1 class="brand-title">Brightwell Care<br>Pharmacy</h1>
  </div>

  <svg class="shapes" viewBox="0 0 851 1200">
    <defs>
      <linearGradient id="photoTone" x1="0" y1="0" x2="1" y2="1">
        <stop offset="0" stop-color="#8b9a5a"/>
        <stop offset=".5" stop-color="#c9a58e"/>
        <stop offset="1" stop-color="#5f6e3c"/>
      </linearGradient>
      <radialGradient id="portraitTone" cx=".5" cy=".45" r=".6">
        <stop offset="0" stop-color="#b88468"/>
        <stop offset="1" stop-color="#4f5d32"/>
      </radialGradient>
    </defs>
    <path d="M650 190 H826 V760 Q826 830 760 840 Q700 845 670 810 Q650 790 650 760 Z" fill="var(--green)"/>
    <path role="img" aria-label="Photo of a smiling senior couple outdoors" d="M28 172 H640 V520 Q560 575 420 540 Q260 500 120 550 Q60 568 28 562 Z" fill="url(#photoTone)"/>
    <path d="M0 945 Q200 890 420 930 Q600 965 851 880 V1200 H0 Z" fill="var(--green)"/>
    <path d="M0 945 Q200 890 420 930 Q600 965 851 880" fill="none" stroke="var(--white)" stroke-width="6"/>
    <circle cx="690" cy="975" r="125" fill="var(--white)"/>
    <circle role="img" aria-label="Photo of a smiling senior couple" cx="690" cy="975" r="114" fill="url(#portraitTone)"/>
  </svg>

  <div class="logo-tab">
    <div class="logo-mark"></div>
    <div class="logo-name">Brightwell Care</div>
  </div>

  <p class="side-note">Lorem ipsum is simply dummy text of the printing and typesetting industry. Lorem ipsum has been the industry's standard dummy text of it</p>

  <section class="service">
    <h2 class="service-title">Blood Pressure Tracking Service</h2>
    <p class="service-lead">Persons that have a card will be able to track their blood pressure online through a secure online blood pressure tracker</p>
  </section>

  <p class="service-body">Lorem Ipsum is simply dummy text of the printing and typesetting industry. Lorem Ipsum has been the industry's standard dummy text ever since the 1500s, when an unknown printer took a galley of type and scrambled it to make a type specimen book. It has survived not only five centuries, but also the leap into electronic typesetting, remaining essentially unchanged. It was popularised in the 1960s with the release of Letraset sheets containing Lorem Ipsum.</p>

  <p class="footer-text">Lorem Ipsum is simply dummy text of the printing and typesetting industry. Lorem Ipsum has been the industry's standard dummy text ever since the 1500s, when an unknown printer took a galley of type and</p>

  <div class="contact">
    <svg viewBox="0 0 24 24" fill="none" stroke="currentColor" stroke-width="2"><circle cx="12" cy="12" r="10"/><path d="M2 12h20M12 2c3 3 3 17 0 20M12 2c-3 3-3 17 0 20"/></svg>
    <span>www.brightwellcare.example</span>
    <span class="gap"></span>
    <svg viewBox="0 0 24 24" fill="currentColor"><path d="M6.6 10.8a15 15 0 0 0 6.6 6.6l2.2-2.2a1 1 0 0 1 1-.25 11.4 11.4 0 0 0 3.6.57 1 1 0 0 1 1 1V20a1 1 0 0 1-1 1A17 17 0 0 1 3 4a1 1 0 0 1 1-1h3.5a1 1 0 0 1 1 1c0 1.25.2 2.45.57 3.57a1 1 0 0 1-.25 1z"/></svg>
    <span>242-555-0148</span>
  </div>
</main>
</body>
</html>
```